Business Card and Letterhead Design for Public Accounting Firm

Business card and letterhead design for a CPA Firm located in Orange County, CA. We're looking for a modern and professional design utilizing our existing logo. We'd like a clean "less is more" look, but also something that catches the eye. We provide a high level of service to our clients. Open to single or double sided business cards.

Additional info: color numbers on logo
Blue :
R 0
G 83
B 125

#00537D

Silver :

R 154
G 154
B 154

#9A9A9A

Target Market(s)

Businesses and individuals

Industry/Entity Type

Accounting

Contact Information for Business Card

Moss Whitfield & Danby LLP - 4827 Larkspur Vale Road, Irvine, CA 92614 - (949)731-2864 - mwdaccts.example

Font styles to use
Serif
Sans Serif
Other font styles liked:
• See font file uploaded

Colors
0054AA
0677BA
7BADD7
CADEEF
E8F1F8

Requirements
Nice to have
• Possibly use the font file provided which matches our logo, but adjust to be not in all caps

```html
<!DOCTYPE html>
<html lang="en">
<head>
<meta charset="utf-8">
<title>Moss Whitfield &amp; Danby LLP – Business Card</title>
<link rel="stylesheet" href="https://fonts.googleapis.com/css2?family=Libre+Baskerville:wght@400;700&display=swap">
<style>
  :root {
    --backdrop: #979797;
    --brand-blue: #00537D;
    --brand-blue-deep: #0B4766;
    --silver: #9A9A9A;
    --paper: #FFFFFF;
    --rule: #A3A3A3;
  }
  * { margin: 0; padding: 0; box-sizing: border-box; }
  html, body {
    width: 1200px; height: 1000px; overflow: hidden;
    background: var(--backdrop);
    font-family: "Libre Baskerville", Georgia, serif;
  }
  .canvas { position: relative; width: 1200px; height: 1000px; }
  .card {
    position: absolute; left: 293px; width: 615px; height: 351px;
    border-radius: 28px;
  }
  .card--back {
    top: 107px; background: var(--brand-blue);
    display: flex; align-items: center; justify-content: center;
  }
  .card--back .wordmark {
    color: var(--brand-blue-deep); font-size: 26px; font-weight: 400;
    letter-spacing: 0.5px;
  }
  .card--front { top: 528px; background: var(--paper); }
  .front-mark {
    position: absolute; left: 37px; top: 66px;
    display: flex; align-items: center; gap: 10px;
  }
  .front-mark .square { width: 16px; height: 16px; background: var(--brand-blue); }
  .front-mark .wordmark { color: var(--brand-blue); font-size: 19px; }
  .firm-name {
    position: absolute; left: 37px; top: 148px;
    color: var(--brand-blue); font-size: 15px; font-weight: 700; letter-spacing: 0.3px;
  }
  .address {
    position: absolute; left: 37px; top: 195px;
    color: var(--silver); font-size: 16px; line-height: 22px; font-style: normal;
  }
  .divider {
    position: absolute; left: 37px; right: 45px; top: 270px;
    border: 0; border-top: 1px solid var(--rule);
  }
  .phone {
    position: absolute; left: 37px; top: 288px;
    color: var(--silver); font-size: 15px; font-weight: 700;
  }
  .website {
    position: absolute; right: 45px; top: 284px;
    color: var(--silver); font-size: 15px;
  }
  .website strong { color: var(--brand-blue); font-weight: 700; }
</style>
</head>
<body>
<main class="canvas">
  <section class="card card--back" aria-label="Card back">
    <span class="wordmark">Moss Whitfield &amp; Danby LLP</span>
  </section>

  <section class="card card--front" aria-label="Card front">
    <div class="front-mark">
      <span class="square"></span>
      <span class="wordmark">Moss Whitfield &amp; Danby LLP</span>
    </div>
    <h1 class="firm-name">Moss Whitfield &amp; Danby LLP</h1>
    <address class="address">4827 Larkspur Vale Road<br>Irvine, CA 92614</address>
    <hr class="divider">
    <p class="phone">(949) 731-2864</p>
    <p class="website"><strong>mwdaccts</strong>.example</p>
  </section>
</main>
</body>
</html>
```